Moxtrel Compensation Lawyers

We need a modern, sleek letterhead that is professional.

In relation to the footer, we would like to have firm contact details there ideally, however you must also insert at the bottom of each page the following....

Liability limited by a scheme approved under the Professional Standards Legislation.

From the attachment you can extract the firm logo. Also, I would like the Accredited specialist circle on the letterhead also.

Also, I would like you to create a document that can easily be edited for change of contact details, as these are likely to change.

Industry/Entity Type

It Professional

Font styles to use
Sans Serif

Colors
0655a3
3276b5
85abd2
0492cd
33a6d7
85cae6
cee9f5
eaf1f7
cbcbcb

Requirements
Must have
• Ph: 9317-2856
• F: 9184-3720
• M 0435-618-294
• kp@moxtrel.com.au
• www.moxtrel.com.au
Nice to have
• the word document gives you an idea of what I like. I am happy for your to amaze me with your creativity.

```html
<!DOCTYPE html>
<html lang="en">
<head>
<meta charset="utf-8">
<title>Moxtrel Compensation Lawyers – Letterhead</title>
<link rel="stylesheet" href="https://fonts.googleapis.com/css2?family=Open+Sans:wght@400&family=Arimo:wght@400&display=swap">
<style>
  :root {
    --backdrop: #1c1c1c;
    --paper: #fbfbfd;
    --brand-band: #1d4fd8;
    --brand-blue: #1f55d6;
    --mark-tint: #85cae6;
    --watermark: #eaf1f7;
    --ink: #111111;
    --footer-ink: #4a4a4a;
    --rule: #cbcbcb;
    --badge-ring: #0655a3;
  }
  html, body {
    margin: 0;
    padding: 0;
    width: 1200px;
    height: 1200px;
    overflow: hidden;
    background: var(--backdrop);
  }
  .letterhead {
    position: absolute;
    left: 161px;
    top: 50px;
    width: 878px;
    height: 1100px;
    background: var(--paper);
    overflow: hidden;
  }
  .top-band {
    position: absolute;
    left: 0; top: 0;
    width: 100%;
    height: 14px;
    background: var(--brand-band);
  }
  .brand {
    position: absolute;
    left: 94px;
    top: 62px;
  }
  .brand-dot {
    width: 58px;
    height: 58px;
    border-radius: 50%;
    background: var(--mark-tint);
    margin-left: 12px;
    margin-bottom: 14px;
  }
  .brand-name {
    margin: 0;
    font-family: "Open Sans", sans-serif;
    font-weight: 400;
    font-size: 28px;
    line-height: 33px;
    color: var(--brand-blue);
    letter-spacing: -0.3px;
  }
  .practice-areas {
    position: absolute;
    left: 564px;
    top: 90px;
    margin: 0;
    padding: 0;
    list-style: none;
    font-family: "Arimo", sans-serif;
    font-size: 19px;
    line-height: 26.5px;
    color: var(--ink);
    letter-spacing: 0.3px;
  }
  .practice-areas li::before {
    content: "•";
    margin-right: 6px;
  }
  .watermark {
    position: absolute;
    left: 270px;
    top: 400px;
    width: 400px;
    height: 400px;
  }
  .footer {
    position: absolute;
    left: 100px;
    top: 1030px;
    width: 640px;
    font-family: "Arimo", sans-serif;
    color: var(--footer-ink);
    text-align: center;
  }
  .footer .office,
  .footer .contacts {
    margin: 0;
    font-size: 15px;
    line-height: 21px;
    letter-spacing: 0.3px;
    white-space: nowrap;
  }
  .footer .rule {
    height: 0;
    width: 580px;
    border-top: 1.5px solid var(--rule);
    margin: 3px auto 4px;
  }
  .footer .liability {
    margin: 0;
    font-size: 11.5px;
    letter-spacing: 0.4px;
    white-space: nowrap;
  }
  .accreditation {
    position: absolute;
    left: 752px;
    top: 1032px;
    width: 58px;
    height: 58px;
  }
</style>
</head>
<body>
  <main class="letterhead">
    <div class="top-band"></div>

    <header class="brand">
      <div class="brand-dot"></div>
      <p class="brand-name">Moxtrel<br>Compensation Lawyers</p>
    </header>

    <ul class="practice-areas">
      <li>INSURANCE LAW</li>
      <li>ESTATE &amp; PROPERTY LAW</li>
      <li>FAMILY LAW</li>
      <li>COMMERCIAL LAW</li>
    </ul>

    <svg class="watermark" viewBox="0 0 400 400" aria-hidden="true">
      <circle cx="200" cy="200" r="190" fill="var(--watermark)"/>
    </svg>

    <footer class="footer">
      <p class="office">Harlowfield Office : P.O. Box B415 Kendrick Vale NSW 2147 &nbsp;www.moxtrel.com.au</p>
      <p class="contacts">Ph: 9317-2856 F: 9184-3720 M: 0435-618-294 kp@moxtrel.com.au</p>
      <div class="rule"></div>
      <p class="liability">Liability limited by a scheme approved under the Professional Standards Legislation.</p>
    </footer>

    <svg class="accreditation" viewBox="0 0 60 60" aria-hidden="true">
      <circle cx="30" cy="30" r="28" fill="#ffffff" stroke="var(--badge-ring)" stroke-width="3"/>
      <circle cx="30" cy="30" r="16" fill="var(--badge-ring)"/>
    </svg>
  </main>
</body>
</html>
```